Postcard flyer for body postive dance classes

We need an eye catching double sided A6 postcard for body positive dance classes. The business name is twirlbrightday and already have a rough logo and some text that needs tidying up and putting together. The design needs to be simple and elegant. We are appealing to a diverse range of adult women with or without dance experience to join us in a safe, supportive and creative environment. We would like the design to use black, white and a soft green. The final design should communicate movement, contentment and wholeness. File with information attached.

Target Market(s)

Diverse range of adult women

Industry/Entity Type

Health And Wellness

Font styles to use
Other font styles liked:
• Candara or similar but open to suggestions

Colors
abd036
cadf82
eaf2ce
fffefb
fef9ed
fff3d1
ffffff

Requirements
Must have
• Logo and text provided.
Nice to have
• Sense of movement. Match to website colours and style.
Should not have
• Intimidating perfect body images

```html
<!DOCTYPE html>
<html lang="en">
<head>
<meta charset="utf-8">
<title>twirlbrightday – postcard</title>
<link href="https://fonts.googleapis.com/css2?family=Cabin:ital,wght@0,400;0,600;0,700;1,500&display=swap" rel="stylesheet">
<style>
  :root {
    --page-bg: #ececea;
    --card: #ffffff;
    --ink: #3b3b3b;
    --ink-soft: #555555;
    --green: #abd036;
    --green-soft: #cadf82;
    --green-pale: #eaf2ce;
    --rule: #b5b5b5;
    --photo-light: #c9c9c9;
    --photo-dark: #5a5a5a;
  }
  * { box-sizing: border-box; margin: 0; padding: 0; }
  html, body { width: 890px; height: 1200px; overflow: hidden; }
  body {
    background: var(--page-bg);
    font-family: "Cabin", "Candara", sans-serif;
    color: var(--ink);
    position: relative;
  }
  .postcard {
    position: absolute;
    left: 113px;
    width: 664px;
    height: 472px;
    background: var(--card);
    box-shadow: 0 3px 10px rgba(0,0,0,.18);
    overflow: hidden;
  }
  .postcard--front { top: 80px; }
  .postcard--back { top: 596px; }

  /* Front */
  .front-art { position: absolute; inset: 0; }
  .green-band {
    position: absolute; left: 0; top: 196px;
    width: 330px; height: 148px;
    background: var(--green-pale);
  }
  .headline {
    position: absolute; left: 28px; top: 46px;
    font-size: 19.5px; font-weight: 400;
  }
  .headline em { font-style: normal; color: var(--green); }
  .intro, .invite, .tagline {
    position: absolute; left: 28px;
    font-size: 16px; line-height: 21px;
    color: var(--ink-soft);
  }
  .intro { top: 94px; width: 270px; }
  .invite { top: 216px; width: 280px; color: var(--ink); }
  .invite strong { font-weight: 700; }
  .tagline { top: 364px; width: 230px; color: var(--ink); }
  .site {
    position: absolute; left: 28px; top: 430px;
    font-size: 15.5px; font-weight: 700; color: var(--ink);
  }
  .brand-badge {
    position: absolute; left: 259px; top: 324px;
    width: 114px; height: 114px; border-radius: 50%;
    background: var(--card);
    border: 5px solid #e4e4e4;
    box-shadow: 0 1px 4px rgba(0,0,0,.2);
    display: flex; align-items: center; justify-content: center;
    font-size: 13px; font-weight: 600; color: var(--ink-soft);
  }
  .photo-caption {
    position: absolute; right: 18px; bottom: 14px;
    font-size: 15px; font-style: italic; font-weight: 500;
    color: #ffffff; letter-spacing: .6px;
  }

  /* Back */
  .brand-title {
    position: absolute; left: 38px; top: 30px;
    font-size: 30px; font-weight: 400; letter-spacing: 1.5px;
    color: var(--ink-soft);
  }
  .contact {
    position: absolute; left: 38px; top: 92px;
    font-size: 15px; line-height: 18.5px; color: var(--ink-soft);
    list-style: none;
  }
  .stamp-box {
    position: absolute; left: 558px; top: 21px;
    width: 84px; height: 62px;
    border: 1.5px solid var(--rule);
  }
  .address-line {
    position: absolute; left: 416px; width: 226px;
    border-top: 1.5px solid var(--rule);
  }
  .brand-watermark {
    position: absolute; left: 36px; top: 318px;
    font-size: 30px; font-weight: 600; color: #ececec;
  }
</style>
</head>
<body>

<section class="postcard postcard--front">
  <svg class="front-art" width="664" height="472" viewBox="0 0 664 472" role="img" aria-label="Black and white photograph of a young woman in a striped top stretching one leg up against a barre in a bright studio">
    <defs>
      <linearGradient id="photoTone" x1="0" y1="0" x2="1" y2="1">
        <stop offset="0" stop-color="var(--photo-light)"/>
        <stop offset=".55" stop-color="#9a9a9a"/>
        <stop offset="1" stop-color="var(--photo-dark)"/>
      </linearGradient>
    </defs>
    <polygon points="376,0 664,0 664,472 290,472" fill="url(#photoTone)"/>
    <polygon points="348,0 376,0 290,472 274,472" fill="var(--green-soft)"/>
  </svg>
  <div class="green-band"></div>

  <h1 class="headline">Dance is <em>JOY,</em> dance is <em>LOVE.</em></h1>
  <p class="intro">Dance is at the core of our being, a celebration of movement, vitality and wholeness.</p>
  <p class="invite">If you’ve never danced before and always wanted to or you want to reignite your past love of dance, join us at <strong>twirlbrightday</strong> to start your journey.</p>
  <p class="tagline">Flow with life through your inner dancer.</p>
  <p class="site">www.twirlbrightday.com.au</p>

  <div class="brand-badge">twirlbrightday</div>
  <p class="photo-caption">movement, contentment, wholeness</p>
</section>

<section class="postcard postcard--back">
  <h2 class="brand-title">twirlbrightday</h2>
  <ul class="contact">
    <li>Contact</li>
    <li>E: mia@twirlbrightday.com.au</li>
    <li>P:0400555018</li>
    <li>www.twirlbrightday.com.au</li>
    <li>Brightvale/Eastholm</li>
  </ul>
  <div class="stamp-box"></div>
  <div class="address-line" style="top:210px"></div>
  <div class="address-line" style="top:255px"></div>
  <div class="address-line" style="top:301px"></div>
  <div class="brand-watermark">twirlbrightday</div>
</section>

</body>
</html>
```